sydney wedding photography business needs a business card design

we need a business card design for a sydney based wedding photography and videography business. our business name is :golden hour photography and video. our target clients are 24-35 yrs female. our style is candid, organic, natural, dynamic. we are a team of young photographers and videographers, and help brides to create memories that they will cherish for the rest of their lives. the logo will be provided. we want an elegant design that reflects our style, and also want to give a great impression to our clients that we are one of the best studios in sydney and our brand means quality and premium service.

Target Market(s)

bride to be, 24-35 years old, living in sydney and surrunding areas

Industry/Entity Type

Wedding Photography

Contact Information for Business Card

address: 57 marrow lane, bexton nsw 2041
mobile: 0431872056
phone: (02) 9361 2748
info@goldenhourstudio.net.au
www.goldenhourstudio.net.au
facebook:goldenhourbridals
instagram:goldenhourbridals

Font styles to use
Serif
Sans Serif

Requirements
Nice to have
• maybe add my slogan"moments kept in soft light" if the layout looks good
Should not have
• no black color, not good idea for wedding biz card

```html
<!DOCTYPE html>
<html lang="en">
<head>
<meta charset="utf-8">
<title>Golden Hour Photography – Business Card</title>
<link rel="stylesheet" href="https://fonts.googleapis.com/css2?family=Lato:wght@400;700&family=Arimo:wght@400;700&display=swap">
<style>
  :root {
    --navy: #0f3260;
    --navy-deep: #002a5a;
    --navy-light: #0e3f73;
    --gold: #d4a20a;
    --gold-bright: #f2c11a;
    --ink: #0c2d5a;
    --paper: #ffffff;
    --paper-shade: #f1f2f4;
  }
  * { margin: 0; padding: 0; box-sizing: border-box; }
  html, body { width: 1149px; height: 1200px; overflow: hidden; }
  body {
    position: relative;
    background: linear-gradient(135deg, #ffffff 0%, #bdbdbd 40%, #8f8f8f 70%, #5a5a5a 100%);
    font-family: "Arimo", Arial, sans-serif;
  }
  .card {
    position: absolute;
    left: 199px;
    width: 754px;
    height: 433px;
    overflow: hidden;
  }
  .card-front { top: 127px; }
  .card-back { top: 620px; background: var(--paper); }

  .front-backdrop {
    position: absolute; inset: 0;
    background: radial-gradient(ellipse at 30% 80%, var(--navy-light) 0%, var(--navy) 70%);
  }
  .brand {
    position: absolute; left: 0; right: 0; top: 163px;
    text-align: center;
    font-family: "Lato", sans-serif;
    font-weight: 700;
    font-size: 44px;
    color: var(--gold);
  }
  .slogan {
    position: absolute; left: 0; right: 0; top: 268px;
    text-align: center;
    font-family: "Lato", sans-serif;
    font-size: 21px;
    color: var(--gold);
  }

  .back-band {
    position: absolute; left: 0; top: 0; width: 100%; height: 207px;
    background: radial-gradient(ellipse at 50% 0%, #0a4482 0%, var(--navy-deep) 60%);
  }
  .person-name {
    position: absolute; left: 0; right: 0; top: 42px;
    text-align: center;
    font-weight: 700;
    font-size: 86px;
    line-height: 1;
    color: var(--gold);
    background: linear-gradient(100deg, var(--gold) 40%, var(--gold-bright) 55%, var(--gold) 70%);
    -webkit-background-clip: text; background-clip: text;
    -webkit-text-fill-color: transparent;
  }
  .person-role {
    position: absolute; left: 0; right: 0; top: 140px;
    text-align: center;
    font-weight: 700;
    font-size: 21px;
    color: var(--gold);
  }
  .back-backdrop {
    position: absolute; left: 0; top: 207px; width: 100%; height: 226px;
    background: linear-gradient(180deg, var(--paper) 0%, var(--paper-shade) 100%);
  }
  .contact {
    position: absolute;
    display: flex; align-items: center; gap: 9px;
    font-weight: 700; font-size: 13px; line-height: 16.5px;
    color: var(--ink);
  }
  .contact-icon { width: 45px; height: 45px; flex: none; }
  .contact-address { left: 76px; top: 241px; }
  .contact-phone { left: 385px; top: 239px; }
  .contact-web { left: 78px; top: 348px; }
  .contact-email { left: 386px; top: 347px; }
  .contact-email .contact-icon { margin-right: 3px; }
</style>
</head>
<body>

<section class="card card-front">
  <div class="front-backdrop" role="img" aria-label="Deep navy background with a faint hexagon pattern"></div>
  <div class="brand">Golden Hour Photography</div>
  <p class="slogan">"moments kept in soft light"</p>
</section>

<section class="card card-back">
  <div class="back-band"></div>
  <h1 class="person-name">NAME</h1>
  <p class="person-role">PHOTOGRAPHER &amp; VEDIOGRAPHER</p>
  <div class="back-backdrop" role="img" aria-label="White background with a faint light grey hexagon pattern"></div>

  <div class="contact contact-address">
    <svg class="contact-icon" viewBox="0 0 45 45">
      <circle cx="22.5" cy="22.5" r="22" fill="var(--navy-deep)"/>
      <path d="M22.5 12a6 6 0 0 0-6 6c0 4.5 6 11 6 11s6-6.5 6-11a6 6 0 0 0-6-6z" fill="none" stroke="#fff" stroke-width="2"/>
      <circle cx="22.5" cy="18" r="2" fill="#fff"/>
      <ellipse cx="22.5" cy="32" rx="7" ry="2.2" fill="none" stroke="#fff" stroke-width="1.6"/>
    </svg>
    <span>57 marrow lane, bexton nsw 2041.</span>
  </div>

  <div class="contact contact-phone">
    <svg class="contact-icon" viewBox="0 0 45 45">
      <circle cx="22.5" cy="22.5" r="21" fill="none" stroke="var(--navy-deep)" stroke-width="3"/>
      <path d="M15 14c2-2 3.5-1 4.5 1l1.5 3c.5 1.2 0 2-1 2.7-.8.6-.5 1.8.5 3.2 1.2 1.6 2.5 2.6 3.5 2.2 1-.5 1.8-1.4 3-.8l3 1.8c1.6 1 1.8 2.4-.2 4.3-2.5 2.3-7 .3-11-4.3S12.8 16.3 15 14z" fill="var(--navy-deep)"/>
      <path d="M25 12a9 9 0 0 1 8 8M25 16.5a5 5 0 0 1 4 4" fill="none" stroke="var(--navy-deep)" stroke-width="2" stroke-linecap="round"/>
    </svg>
    <span>mobile: 0431872056<br>phone: (02) 9361 2748</span>
  </div>

  <div class="contact contact-web">
    <svg class="contact-icon" viewBox="0 0 45 45">
      <circle cx="22.5" cy="22.5" r="22" fill="var(--navy-deep)"/>
      <g fill="none" stroke="#fff" stroke-width="1.6">
        <circle cx="22.5" cy="22.5" r="12"/>
        <ellipse cx="22.5" cy="22.5" rx="5.5" ry="12"/>
        <path d="M10.5 22.5h24M12.5 16h20M12.5 29h20M22.5 10.5v24"/>
      </g>
    </svg>
    <span>www.goldenhourstudio.net.au<br>facebook:goldenhourbridals<br>instagram:goldenhourbridals</span>
  </div>

  <div class="contact contact-email">
    <svg class="contact-icon" viewBox="0 0 45 45">
      <circle cx="22.5" cy="22.5" r="22" fill="var(--navy-deep)"/>
      <rect x="12" y="16" width="21" height="14" fill="#fff"/>
      <path d="M12 16l10.5 8 10.5-8" fill="none" stroke="var(--navy-deep)" stroke-width="1.8"/>
    </svg>
    <span>info@goldenhourstudio.net.au</span>
  </div>
</section>

</body>
</html>
```